DL FLYER - Roam Sip Nibble Trails

I need a2-sided DL flyer designed to put into Hotel foyers. This will need to stand out as it will be in a rack with multiple other options.

Our tours are all about walking with us to take in great venues for food and beverages with art and history along the way.

We operate in Perth City plus Fremantle.

I am hoping for the flyer to look something like my website - https://roamsipnibble.example.au/

This website will be updated in the coming weeks with new experiences and a new booking platform.

I want the flyers to be used to drive bookings from the updated website.

Attached are several images that could be used also.

Target Market(s)

Social groups, couples, friends groups & foodies!

Industry/Entity Type

Food & Beverage Walking Tours

Font styles to use
Serif
Sans Serif
Decorative
Script

Colors
0094D4
00A9DD
6FCCEA
C7EBF8
E9F6FB
59FF00
82FF00
B8FF75
E3FFCB
F4FFEA
FFF300
FFF600
FEFA6F
FFFEC7
FFFEE8
F0912C
F2A743
F7CA91
FBE8D2
FDF5EE

Requirements
Must have
• Logo and must look fun. Discount code - TOWNISFAB for online price 15% off (not valid on gift voucher purchases)
Nice to have
• similar to my website - colours and styling. I will be updating available tours, costs and timing in the coming weeks. Check out my new booking link to get pricing and tour details - https://www-628k.reservix.example/reservix/b_roamsipnibbletrails_start.html?ctlsrc2=Qm392LAZPT8RNbo5JuvxK3hcW%2F7T6OyvqpeDd%2FMzRj%3D&src=09k
Should not have
• .

```html
<!DOCTYPE html>
<html lang="en">
<head>
<meta charset="utf-8">
<title>Roam Sip Nibble Trails – DL Flyer</title>
<link rel="stylesheet" href="https://fonts.googleapis.com/css2?family=Anton&family=Montserrat:wght@500;600;700;800&display=swap">
<style>
:root{
  --orange:#F0912C;
  --orange-deep:#E0621A;
  --orange-soft:#F7CA91;
  --orange-pale:#FBE8D2;
  --ink:#2F4744;
  --pill:#E9ECEC;
  --paper:#FFFFFF;
  --bg:#EFEAE4;
}
*{box-sizing:border-box;margin:0;padding:0}
html,body{width:1200px;height:750px;overflow:hidden;background:var(--bg)}
body{position:relative;font-family:"Montserrat",sans-serif;color:var(--ink)}
.flyer{position:absolute;top:25px;width:330px;height:700px;background:var(--paper);overflow:hidden;box-shadow:0 6px 18px rgba(0,0,0,.15)}
.flyer--front{left:255px}
.flyer--back{left:615px}
.photo{position:absolute;display:block}
.photo--round{border-radius:50%;border:3px solid var(--paper);box-shadow:0 0 0 1.5px var(--orange)}
.brand{position:absolute;display:flex;align-items:center;gap:7px;font-family:"Montserrat",sans-serif;font-weight:800;font-size:13px;line-height:1.05;color:var(--ink)}
.brand__dot{width:22px;height:22px;border-radius:50%;background:var(--orange);flex:none}
.headline{position:absolute;left:0;right:0;text-align:center;font-family:"Anton",sans-serif;text-transform:uppercase}
.headline__big{font-size:66px;line-height:1;background:linear-gradient(180deg,var(--orange) 0%,var(--orange-deep) 100%);-webkit-background-clip:text;background-clip:text;color:transparent}
.headline__sub{font-size:14px;color:var(--ink);letter-spacing:.3px;margin-top:2px}
.headline__accent{font-size:33px;line-height:1.05;color:var(--orange-deep)}
.intro{position:absolute;left:22px;right:22px;top:548px;font-size:8.6px;line-height:1.45;text-align:center;color:#555}
.features{position:absolute;left:14px;right:14px;top:594px;display:flex;justify-content:space-between}
.feature{width:96px;text-align:center;font-family:"Montserrat",sans-serif;font-weight:800;font-size:10px;line-height:1.15;color:var(--ink)}
.feature__icon{width:36px;height:36px;border-radius:50%;margin:0 auto 4px;border:1.5px solid var(--orange-soft);display:flex;align-items:center;justify-content:center;background:var(--paper)}
.contact{position:absolute;left:10px;right:10px;bottom:12px;display:flex;align-items:center;gap:8px}
.book{display:flex;align-items:center;gap:5px;background:linear-gradient(90deg,var(--orange-deep),var(--orange));color:var(--paper);padding:4px 8px;border-radius:3px}
.book__text{font-family:"Montserrat",sans-serif;line-height:1}
.book__cta{display:block;font-weight:800;font-size:12px;color:var(--ink)}
.book__url{display:block;font-weight:700;font-size:7.5px}
.phone{display:flex;align-items:center;gap:3px;font-family:"Anton",sans-serif;font-size:25px;color:var(--orange-deep);line-height:1}
.section-title{position:absolute;right:20px;top:300px;text-align:right;font-family:"Anton",sans-serif;font-size:30px;line-height:1.02;color:var(--orange-deep);text-transform:uppercase}
.tours{position:absolute;left:12px;top:382px;width:306px;border-collapse:separate;border-spacing:3px 3px;font-size:7.6px;font-weight:600}
.tours th{background:var(--ink);color:var(--paper);font-size:7.6px;font-weight:700;letter-spacing:.5px;padding:3px 4px;border-radius:8px}
.tours td{background:var(--pill);padding:3px 5px;border-radius:8px;white-space:nowrap;text-align:center}
.tours td:first-child{text-align:left}
.ticket{position:absolute;left:14px;top:500px;width:302px;height:104px}
.ticket svg{position:absolute;inset:0}
.ticket__text{position:absolute;inset:0;display:flex;flex-direction:column;align-items:center;justify-content:center;text-align:center}
.ticket__code{font-family:"Anton",sans-serif;font-size:46px;line-height:1;color:var(--ink);letter-spacing:1px}
.ticket__offer{font-weight:800;font-size:15px;color:var(--ink);margin-top:2px}
.ticket__note{font-weight:700;font-size:8px;color:var(--ink)}
</style>
</head>
<body>

<section class="flyer flyer--front" aria-label="Flyer front">
  <div class="photo" role="img" aria-label="Friends sharing food and wine at a warmly lit restaurant table" style="left:0;top:0;width:330px;height:320px;background:linear-gradient(180deg,#d9cfc6 0%,#c99a72 45%,#e7b98a 70%,#ffffff 100%)"></div>
  <div class="photo" role="img" aria-label="Soft city skyline fading behind the text" style="left:0;top:520px;width:330px;height:180px;background:linear-gradient(180deg,#ffffff 0%,#e4e4e4 60%,#cfcfcf 100%)"></div>

  <div class="brand" style="right:12px;top:70px;background:rgba(255,255,255,.9);padding:6px 8px;border-radius:4px">
    <span class="brand__dot"></span><span>Roam Sip<br>Nibble Trails</span>
  </div>

  <div class="headline" style="top:250px">
    <div class="headline__big">Walking</div>
    <div class="headline__sub">With us to take in great venues for</div>
    <div class="headline__accent">Food &amp; Beverages</div>
  </div>

  <div class="photo photo--round" role="img" aria-label="Cocktails being poured at a bar" style="left:14px;top:390px;width:126px;height:126px;background:radial-gradient(circle at 40% 40%,#c98a5a,#5b3a2a)"></div>
  <div class="photo photo--round" role="img" aria-label="Golden fried bites with a creamy dip" style="left:184px;top:382px;width:114px;height:114px;background:radial-gradient(circle at 50% 45%,#e9c27a,#b57b3d)"></div>
  <div class="photo photo--round" role="img" aria-label="Plated dishes on a wooden table" style="left:134px;top:456px;width:82px;height:82px;background:radial-gradient(circle at 50% 50%,#d98b55,#6e4a33)"></div>

  <p class="intro">We take our walking tours down the back streets and through the alleyways, to share great food and drinks. Go with our guides to try modern Australian fare and hear some history about each city.</p>

  <div class="features">
    <div class="feature">
      <div class="feature__icon"><svg width="18" height="22" viewBox="0 0 20 24"><path d="M10 1C5 1 1.5 4.6 1.5 9.2 1.5 15 10 23 10 23s8.5-8 8.5-13.8C18.5 4.6 15 1 10 1z" fill="var(--orange-deep)"/><circle cx="10" cy="9" r="3.3" fill="#fff"/></svg></div>
      Explore the city
    </div>
    <div class="feature">
      <div class="feature__icon"><svg width="22" height="20" viewBox="0 0 24 22"><path d="M12 2C6 2 2 5.6 2 10c0 2.4 1.2 4.5 3.2 5.9L4 20l4.6-2.4c1 .3 2.2.4 3.4.4 6 0 10-3.6 10-8S18 2 12 2z" fill="none" stroke="var(--orange-deep)" stroke-width="2"/><circle cx="8" cy="10" r="1.5" fill="var(--orange-deep)"/><circle cx="12" cy="10" r="1.5" fill="var(--orange-deep)"/><circle cx="16" cy="10" r="1.5" fill="var(--orange-deep)"/></svg></div>
      Enjoy Great food
    </div>
    <div class="feature">
      <div class="feature__icon"><svg width="20" height="20" viewBox="0 0 22 22"><circle cx="11" cy="11" r="9" fill="none" stroke="var(--orange-deep)" stroke-width="2"/><path d="M11 5v6l4 3" fill="none" stroke="var(--orange-deep)" stroke-width="2" stroke-linecap="round"/></svg></div>
      Art and history
    </div>
  </div>

  <div class="contact">
    <div class="book">
      <svg width="14" height="14" viewBox="0 0 14 14"><path d="M2 7h8M7 3l4 4-4 4" fill="none" stroke="#fff" stroke-width="2" stroke-linecap="round"/></svg>
      <span class="book__text"><span class="book__cta">BOOK NOW</span><span class="book__url">roamsipnibble.example.au</span></span>
    </div>
    <div class="phone">
      <svg width="14" height="24" viewBox="0 0 14 24"><rect x="1" y="1" width="12" height="22" rx="2.5" fill="none" stroke="var(--ink)" stroke-width="2"/><line x1="5" y1="20" x2="9" y2="20" stroke="var(--ink)" stroke-width="1.5"/></svg>
      0412 345 678
    </div>
  </div>
</section>

<section class="flyer flyer--back" aria-label="Flyer back">
  <div class="photo" role="img" aria-label="City skyline at sunset with a palm tree" style="left:0;top:470px;width:330px;height:230px;background:linear-gradient(180deg,#ffffff 0%,#f4b27a 22%,#e2722e 55%,#5a3a2c 85%,#ffffff 100%)"></div>

  <div class="photo photo--round" role="img" aria-label="Couple walking arm in arm down a city laneway" style="left:-25px;top:10px;width:240px;height:240px;background:linear-gradient(160deg,#9c8a7e 0%,#b0703f 45%,#2f3640 100%)"></div>
  <div class="photo photo--round" role="img" aria-label="Guests sipping wine on a tour" style="left:-40px;top:170px;width:90px;height:90px;background:radial-gradient(circle,#c7826b,#7b4a3e)"></div>

  <div class="brand" style="right:14px;top:80px">
    <span class="brand__dot"></span><span>Roam Sip<br>Nibble Trails</span>
  </div>
  <div class="photo photo--round" role="img" aria-label="Tour group posing in front of a colourful mural" style="right:22px;top:160px;width:100px;height:100px;background:radial-gradient(circle,#d86a5a,#3d6fa0)"></div>

  <div class="section-title">Tours &amp;<br>Experiences</div>

  <table class="tours">
    <thead>
      <tr><th>PLANS</th><th>TIME</th><th>LOCATION</th><th>RATE</th></tr>
    </thead>
    <tbody>
      <tr><td>Twilight Tasting Stroll</td><td>SAT 4-7 PM</td><td>Perth</td><td>$85</td></tr>
      <tr><td>Harbourside Sunday Sips</td><td>SUN 3-6 PM</td><td>Fremantle</td><td>$75</td></tr>
      <tr><td>Market Basket Ramble</td><td>SAT 1-4 PM</td><td>Fremantle</td><td>$80</td></tr>
      <tr><td>Laneway Lunch Crawl</td><td>SAT 11:45 AM</td><td>Perth</td><td>$75</td></tr>
      <tr><td>Grill &amp; Ale Wander</td><td>SAT 11 AM</td><td>Perth</td><td>$85</td></tr>
    </tbody>
  </table>

  <div class="ticket">
    <svg viewBox="0 0 302 104" width="302" height="104" aria-hidden="true">
      <defs><linearGradient id="ticketFill" x1="0" y1="0" x2="0" y2="1"><stop offset="0" stop-color="#F2A743"/><stop offset="1" stop-color="#E0621A"/></linearGradient></defs>
      <path d="M14 0H288a14 14 0 0 0 14 14V38a14 14 0 0 0 0 28V90a14 14 0 0 0-14 14H14A14 14 0 0 0 0 90V66a14 14 0 0 0 0-28V14A14 14 0 0 0 14 0z" fill="url(#ticketFill)"/>
    </svg>
    <div class="ticket__text">
      <div class="ticket__code">TOWNISFAB</div>
      <div class="ticket__offer">ONLINE PRICE 15% OFF</div>
      <div class="ticket__note">(NOT VALID ON GIFT VOUCHER PURCHASES)</div>
    </div>
  </div>

  <div class="contact">
    <div class="book">
      <svg width="14" height="14" viewBox="0 0 14 14"><path d="M2 7h8M7 3l4 4-4 4" fill="none" stroke="#fff" stroke-width="2" stroke-linecap="round"/></svg>
      <span class="book__text"><span class="book__cta">BOOK NOW</span><span class="book__url">roamsipnibble.example.au</span></span>
    </div>
    <div class="phone">
      <svg width="14" height="24" viewBox="0 0 14 24"><rect x="1" y="1" width="12" height="22" rx="2.5" fill="none" stroke="var(--ink)" stroke-width="2"/><line x1="5" y1="20" x2="9" y2="20" stroke="var(--ink)" stroke-width="1.5"/></svg>
      0412 345 678
    </div>
  </div>
</section>

</body>
</html>
```